Graphic background for 10 Pull Up Banners

To produce a graphic background for a 100 cm wide by 200 cm high Pull-Up Display banner containing a Buddhist text in three languages: Tibetan, Mandarin and English. Please refer to uploaded file "Elements of Pull Up Banner". The design should be simple (not drawing attention away from the text). This design should then be varied for or extended to the next banner and so on until the 10th banner. When the banners are lined up, they should form a single design that is 1000 cm wide by 200 cm high.
An alternative way to look at the project is to produce a graphic background of 1000 cm width by 200 cm height that is then splitted into ten separate 100 cm wide by 200 cm high graphic to be used as background for 10 Buddhist texts (text 1, 2, 3, 4, 5, 6, 7, 8, 9a, 9b) on 10 Pull-Up Display Banners, the text in each banner being in the three languages mentioned earlier.
In either perspective, the design should be simple and not draw attention away from the texts. See uploaded PDF file "Examples.pdf"
For attendees at a Buddhist Event.

```html
<!DOCTYPE html>
<html lang="en">
<head>
<meta charset="utf-8">
<title>Dharma Teachings – Pull-Up Banner Series</title>
<link rel="stylesheet" href="https://fonts.googleapis.com/css2?family=Noto+Sans+SC:wght@400;500&family=Noto+Serif+Tibetan:wght@400;500&family=Open+Sans:wght@400;600&display=swap">
<style>
  :root {
    --page: #ffffff;
    --ink: #ffffff;
    --ink-soft: rgba(255, 255, 255, 0.92);
    --gold: #d9b45a;
    --gold-deep: #a97f2a;
    --emblem-bg: #fbf6f0;
    --emblem-ink: #c7473e;
    --rule: rgba(255, 255, 255, 0.85);
    --font-tibetan: "Noto Serif Tibetan", serif;
    --font-chinese: "Noto Sans SC", sans-serif;
    --font-latin: "Open Sans", sans-serif;
  }
  * { box-sizing: border-box; margin: 0; padding: 0; }
  html, body { width: 1200px; height: 590px; overflow: hidden; background: var(--page); }
  .series { position: relative; width: 1200px; height: 590px; }

  .banner { position: absolute; top: 0; width: 294px; height: 590px; overflow: hidden; color: var(--ink); text-align: center; }
  .banner--1 { left: 0; }
  .banner--2 { left: 302px; }
  .banner--3 { left: 604px; }
  .banner--4 { left: 906px; }

  .scenery { position: absolute; inset: 0; }
  .banner--1 .scenery { background:
      radial-gradient(ellipse 70% 40% at 20% 95%, rgba(70,20,10,0.75), transparent 70%),
      linear-gradient(180deg, #b9702a 0%, #d88d2a 30%, #e9a33a 48%, #e0782a 65%, #c44a22 82%, #8f2b16 100%); }
  .banner--2 .scenery { background:
      linear-gradient(180deg, #a99232 0%, #c9a635 25%, #e9b53c 45%, #f0a033 58%, #e47428 72%, #cf4d22 88%, #a9361a 100%); }
  .banner--3 .scenery { background:
      linear-gradient(180deg, #c59a30 0%, #deae38 25%, #eeb23a 42%, #f2a33a 55%, #e67a2c 70%, #d3502a 85%, #b23a22 100%); }
  .banner--4 .scenery { background:
      linear-gradient(180deg, #b9b6b2 0%, #d4c4a6 20%, #e8b260 40%, #ee9a3e 55%, #e26e2c 72%, #cd4a24 88%, #a8341c 100%); }

  .border-band { position: absolute; left: 0; right: 0; height: 22px;
    background: linear-gradient(180deg, rgba(233,200,110,0.55), rgba(169,127,42,0.55)); }
  .border-band--top { top: 12px; }
  .border-band--bottom { top: 552px; }

  .emblem { position: absolute; left: 117px; top: 2px; width: 60px; height: 60px; border-radius: 50%;
    background: var(--emblem-bg); box-shadow: 0 0 0 2px rgba(255,255,255,0.6); }

  .title { position: absolute; left: 0; right: 0; top: 63px; font-size: 9px; line-height: 14px; white-space: nowrap; }
  .title .zh { font-family: var(--font-chinese); }
  .title .en { font-family: var(--font-latin); font-weight: 600; }
  .banner--1 .title { font-size: 11px; }
  .rule { position: absolute; left: 36px; right: 36px; height: 1px; background: var(--rule); }
  .rule--short { left: 70px; right: 70px; }

  .block { position: absolute; left: 0; right: 0; }
  .tibetan { font-family: var(--font-tibetan); white-space: nowrap; }
  .chinese { font-family: var(--font-chinese); white-space: nowrap; }
  .english { font-family: var(--font-latin); white-space: nowrap; }
  .note { font-family: var(--font-chinese); white-space: nowrap; color: var(--ink-soft); }
</style>
</head>
<body>
<main class="series">

  <!-- Banner 1 -->
  <section class="banner banner--1">
    <div class="scenery" role="img" aria-label="Sunset sky over snow mountains in orange and red"></div>
    <div class="border-band border-band--top" role="img" aria-label="Gold endless-knot border"></div>
    <div class="emblem" role="img" aria-label="Emblem of a seated Buddha figure"></div>
    <h2 class="title"><span class="zh">十个误解</span> &nbsp;-&nbsp; <span class="en">Ten Mistaking</span></h2>
    <div class="rule" style="top:85px"></div>
    <div class="block tibetan" style="top:100px;font-size:7px;line-height:11px">
      <p>དད་པ་དང་འདོད་པ་ནོར་ཉེན་ཡོད།།</p>
      <p>བྱམས་སྙིང་རྗེ་དང་ཆགས་པ་ནོར་ཉེན་ཡོད།།</p>
      <p>ཤེས་བྱའི་སྟོང་པ་དང་བློས་བྱས་སྟོང་པ་ནོར་ཉེན་ཡོད།།</p>
      <p>ཆོས་ཀྱི་དབྱིངས་དང་ཆད་ལྟ་ནོར་ཉེན་ཡོད།།</p>
      <p>ཉམས་མྱོང་དང་རྟོགས་པ་ནོར་ཉེན་ཡོད།།</p>
      <p>བཙུན་པ་དང་རྒྱལ་པོ་ནོར་ཉེན་ཡོད།།</p>
      <p>འཁྲུལ་ཞིག་དང་བདུད་ཟིན་ནོར་ཉེན་ཡོད།།</p>
      <p>གྲུབ་ཐོབ་དང་གཡོ་ཅན་ནོར་ཉེན་ཡོད།།</p>
      <p>གཞན་དོན་དང་རང་དོན་ནོར་ཉེན་ཡོད།།</p>
      <p>ཐབས་མཁས་དང་གཡོ་སྒྱུ་ནོར་ཉེན་ཡོད།།</p>
    </div>
    <div class="rule rule--short" style="top:228px"></div>
    <div class="block chinese" style="top:244px;font-size:9.5px;line-height:12px">
      <p>信心与爱欲可能混淆，</p>
      <p>慈悲与贪执可能混淆，</p>
      <p>所知¹本空与思维造作空性可能混淆，</p>
      <p>法界与断见²可能混淆，</p>
      <p>觉受与证悟可能混淆，</p>
      <p>尊者与神棍可能混淆，</p>
      <p>破惑与著魔可能混淆，</p>
      <p>成就者与骗子可能混淆，</p>
      <p>利他与自利可能混淆，</p>
      <p>方便善巧与谄媚哄骗可能混淆。</p>
    </div>
    <div class="block note" style="top:370px;font-size:5.5px;line-height:8px">
      <p>1. 所知：可以认识的外境。</p>
      <p>2. 断见：否定因果、前生、后世等说法的见解。</p>
    </div>
    <div class="rule rule--short" style="top:404px"></div>
    <div class="block english" style="top:419px;font-size:5.6px;line-height:10.8px">
      <p>Desire can be mistaken for faith or devotion.</p>
      <p>Attachment can be mistaken for love and compassion.</p>
      <p>Conceptual emptiness can be mistaken for the emptiness of the nature of phenomena.</p>
      <p>Nihilism can be mistaken for the dharmadhatu.</p>
      <p>A meditative experience can be mistaken for realization.</p>
      <p>Outer religious practices can be mistaken for inner development of good qualities.</p>
      <p>A person in the grip of a demon can be mistaken for a person who has destroyed his own delusions.</p>
      <p>A charlatan can be mistaken for a siddha.</p>
      <p>An act to benefit yourself can be mistaken for an act to benefit others.</p>
      <p>Deviousness can be mistaken for skilful means.</p>
    </div>
    <div class="border-band border-band--bottom" role="img" aria-label="Gold endless-knot border"></div>
  </section>

  <!-- Banner 2 -->
  <section class="banner banner--2">
    <div class="scenery" role="img" aria-label="Sunset sky over snow mountains in yellow and orange"></div>
    <div class="border-band border-band--top" role="img" aria-label="Gold endless-knot border"></div>
    <div class="emblem" role="img" aria-label="Emblem of a seated Buddha figure"></div>
    <h2 class="title"><span class="zh">欲与爱</span> &nbsp;-&nbsp; <span class="en" style="font-weight:400">Desire &amp; Attachment</span></h2>
    <div class="rule" style="top:84px"></div>
    <div class="block tibetan" style="top:90px;font-size:14px;line-height:22px">
      <p>འདོད་པ་མེད་ན་རང་དོན་མི་འགྲུབ་ཀྱང་།།</p>
      <p>འདོད་པ་ཡོད་ཚད་ཆགས་པ་མི་ཡིན་པས།།</p>
      <p>འདོད་དང་ཆགས་པའི་ཁྱད་པར་མ་ཤེས་པར།།</p>
      <p>འདོད་ཆགས་ལམ་དུ་ཁྱེར་བ་ཧ་ཅང་རེ།།</p>
    </div>
    <div class="rule rule--short" style="top:198px"></div>
    <div class="block chinese" style="top:228px;font-size:12.5px;line-height:18px">
      <p>若无意欲则不成自利，</p>
      <p>然有意欲非为执着故，</p>
      <p>不知意欲执着差别即，</p>
      <p>贪执说所当取确荒唐。</p>
    </div>
    <div class="rule rule--short" style="top:322px"></div>
    <div class="block english" style="top:345px;font-size:7.8px;line-height:22px">
      <p>If you have no desire, your goal cannot be achieved.</p>
      <p>Since not all desire is attachment,</p>
      <p>not knowing how to differentiate desire from attachment,</p>
      <p>to talk about bringing passion into the path is absurd.</p>
    </div>
    <div class="border-band border-band--bottom" role="img" aria-label="Gold endless-knot border"></div>
  </section>

  <!-- Banner 3 -->
  <section class="banner banner--3">
    <div class="scenery" role="img" aria-label="Sunset sky over mountains and a lake in yellow and red"></div>
    <div class="border-band border-band--top" role="img" aria-label="Gold endless-knot border"></div>
    <div class="emblem" role="img" aria-label="Emblem of a seated Buddha figure"></div>
    <h2 class="title" style="font-size:8.5px"><span class="zh">曾修过佛法的相状</span> &nbsp;-&nbsp; <span class="en" style="font-weight:400">Signs Of Having Practised The Dharma</span></h2>
    <div class="rule" style="top:84px"></div>
    <div class="block tibetan" style="top:88px;font-size:11px;line-height:20px">
      <p>རང་ལུས་ཡོངས་སུ་མི་བརྟེན་ཆོས་ལ་བཏང་ཤེས་ན།།</p>
      <p>དལ་འབྱོར་རིན་ཆེན་སྙིང་པོ་ལོན་པའི་རྟགས།།</p>
      <p>གསེར་དང་འོ་བ་མཉམ་བཞག་སྙོམས་ཤེས་ན།།</p>
      <p>མི་རྟག་སྒྱུ་མ་རྒྱུད་ལ་སྐྱེས་པའི་རྟགས།།</p>
      <p>འཁོར་བའི་ཆོས་ལ་དགྲ་རུ་མཐོང་ཤེས་ན།།</p>
      <p>སྡུག་བསྔལ་རྒྱ་མཚོའི་ཕ་རོལ་འགྲོ་བའི་རྟགས།།</p>
    </div>
    <div class="rule rule--short" style="top:228px"></div>
    <div class="block chinese" style="top:240px;font-size:10px;line-height:12.5px">
      <p>若懂舍自身富而修行，</p>
      <p>表示取得真贵暇满¹义；</p>
      <p style="margin-top:9px">若懂金与土块平等观，</p>
      <p>表示‘无常’‘如幻’心中生；</p>
      <p style="margin-top:9px">若视轮回现象为敌人，</p>
      <p>表示渡往苦海之彼岸。</p>
    </div>
    <div class="block note" style="top:335px;font-size:5.5px;line-height:8px"><p>1 暇满：八有暇和十圆满。</p></div>
    <div class="rule" style="top:352px"></div>
    <div class="block english" style="top:373px;font-size:5.8px;line-height:8.5px">
      <p>If you know not to cherish your body but use it to attain</p>
      <p>accomplishments (in the Dharma),</p>
      <p>it is a sign that you have gotten the essence</p>
      <p>of your precious freedoms and fortunes.</p>
      <p style="margin-top:9px">If you know the sameness of gold and dirt</p>
      <p>while in meditative equipoise, it is a sign that</p>
      <p>the insight of impermanence and illusion have arisen in your mental continuum.</p>
      <p style="margin-top:9px">If you know to see samsaric phenomena as an enemy,</p>
      <p>it is a sign that you are heading to the other shore</p>
      <p>of the ocean of suffering.</p>
      <p style="margin-top:9px">1. Freedom and fortunes: the eight freedoms and ten fortunes</p>
    </div>
    <div class="border-band border-band--bottom" role="img" aria-label="Gold endless-knot border"></div>
  </section>

  <!-- Banner 4 -->
  <section class="banner banner--4">
    <div class="scenery" role="img" aria-label="Clouded sky turning to sunset over snow mountains"></div>
    <div class="border-band border-band--top" role="img" aria-label="Gold endless-knot border"></div>
    <div class="emblem" role="img" aria-label="Emblem of a seated Buddha figure"></div>
    <h2 class="title" style="color:#1e1a16"><span class="zh">上师之恩德</span> &nbsp;-&nbsp; <span class="en" style="font-weight:400">Kindness Of The Guru</span></h2>
    <div class="rule" style="top:90px;background:#1e1a16"></div>
    <div class="block tibetan" style="top:94px;font-size:15px;line-height:24px;color:#1e1a16">
      <p>བླ་མ་བརྗེད་པ་མ་བྱེད་ཅིག།</p>
      <p>སངས་རྒྱས་མང་པོ་བྱོན་གྱུར་ཀྱང་།།</p>
      <p>བདག་ནི་སུ་ཡིས་རྗེས་མ་བཟུང་།།</p>
      <p>ཁྱེད་ཀྱིས་མ་དོར་ཐུགས་རྗེས་བསྐྱངས།།</p>
      <p>སངས་རྒྱས་སྟོང་ལས་ཁྱེད་དྲིན་ཆེ།།</p>
    </div>
    <div class="rule" style="top:222px;background:#1e1a16"></div>
    <div class="block chinese" style="top:242px;font-size:14px;line-height:20.5px;color:#1e1a16">
      <p>切莫忘记上师。</p>
      <p>即使众多佛降临，</p>
      <p>谁皆未曾摄受我，</p>
      <p>您不舍弃悲悯护，</p>
      <p>您比千佛恩更大。</p>
    </div>
    <div class="rule" style="top:356px;background:#1e1a16"></div>
    <div class="block english" style="top:370px;font-size:8.5px;line-height:14px;color:#1e1a16">
      <p>Do not forget the guru.</p>
      <p>Although many Buddhas had appeared,</p>
      <p style="margin-top:6px">none has taken hold of me.</p>
      <p style="margin-top:6px">You did not abandon me, but lovingly and</p>
      <p style="margin-top:6px">compassionately protected me.</p>
      <p style="margin-top:56px">Your kindness is greater than a thousand Buddhas'.</p>
    </div>
    <div class="border-band border-band--bottom" role="img" aria-label="Gold endless-knot border"></div>
  </section>

</main>
</body>
</html>
```